female esthetician looking for an impact business card

I an an expert in skin care industry with high experience in NYC.I want my business card to look professional , an impact at first look. I do want a combination between white and gold . I believe the font will be great if is gold.. The Fonts are also important. MIRELA COSTANDI (SKIN CARE BOUTIQUE)

THIS SHOULD BE THE BUSINESS NAME, and should be placed on th eback of the card.
IN front m, the name MIRELA COSTANDI - ESTHETCIAN

BY APPOINTMENTS ONLY: 512.478.2936

Target Market(s)

HIGH END CLIENTELE

Contact Information for Business Card

iT WILL BE on a luxury paper. I neeed the wow feeling

Requirements
Should not have
• pictures

```html
<!DOCTYPE html>
<html lang="en">
<head>
<meta charset="utf-8">
<title>Mirela Costandi – Business Card</title>
<link rel="stylesheet" href="https://fonts.googleapis.com/css2?family=Cinzel:wght@400&family=Lato:wght@400&display=swap">
<style>
  :root {
    --backdrop: #2e2a28;
    --card: #ffffff;
    --gold: #f2b705;
    --rule: #e4e4e4;
  }
  * { box-sizing: border-box; margin: 0; padding: 0; }
  html, body {
    width: 1200px;
    height: 844px;
    overflow: hidden;
    background: var(--backdrop);
  }
  .canvas {
    position: relative;
    width: 1200px;
    height: 844px;
    display: flex;
    align-items: center;
    justify-content: center;
    gap: 60px;
  }
  .card {
    width: 520px;
    height: 300px;
    background: var(--card);
    display: flex;
    flex-direction: column;
    align-items: center;
    justify-content: center;
    text-align: center;
    color: var(--gold);
  }
  .card-front .holder-name {
    font-family: "Cinzel", serif;
    font-size: 28px;
    letter-spacing: 1px;
    line-height: 1;
  }
  .card-front .holder-title {
    font-family: "Cinzel", serif;
    font-size: 13px;
    letter-spacing: 1px;
    margin-top: 6px;
  }
  .card-front .divider {
    width: 230px;
    height: 1px;
    background: var(--rule);
    margin: 16px 0 14px;
  }
  .card-front .availability {
    font-family: "Cinzel", serif;
    font-size: 16px;
    letter-spacing: 0.5px;
  }
  .card-front .phone,
  .card-front .email {
    font-family: "Lato", sans-serif;
    font-size: 18px;
    margin-top: 6px;
  }
  .card-back .brand-name {
    font-family: "Cinzel", serif;
    font-size: 38px;
    letter-spacing: 1px;
    line-height: 1;
  }
  .card-back .brand-tagline {
    font-family: "Cinzel", serif;
    font-size: 12px;
    letter-spacing: 7px;
    margin-top: 8px;
  }
</style>
</head>
<body>
  <main class="canvas">
    <section class="card card-front">
      <h1 class="holder-name">MIRELA COSTANDI</h1>
      <p class="holder-title">ESTHETCIAN</p>
      <div class="divider"></div>
      <p class="availability">BY APPOINTMENTS ONLY</p>
      <p class="phone">512.478.2936</p>
      <p class="email">mirelacostandi@studiomail.com</p>
    </section>
    <section class="card card-back">
      <h2 class="brand-name">MIRELA COSTANDI</h2>
      <p class="brand-tagline">SKIN CARE BOUTIQUE</p>
    </section>
  </main>
</body>
</html>
```